Book Cover for: TITLE Mend the Quiet Hours SUBTITLE For couples who don't want to break up

We need a full cover design for a book on relationships written by husband and wife team, Marla and Walter Dunmore, PhD. This book will offer hope for couples that are on the verge of breaking up but want to work things out and stay together. The theme is to teach couples about their own reactions to their partner, how moods affect a relationship, how to get creative to solving problems and how to have a good feeling towards your partner regardless of differences. This book is about hope. It is a positive look at relationships that feel hopeless.

Target Market(s)

Married or couples that are going through a difficult time and are considering splitting up due to, communication difficulties, addiction, affair. We imagine the book will appeal to women more than men but still want a cover that men would be comfortable picking up.

Colors

Designer to choose colors to be used in the design.

Requirements
Must have
• We want the cover to beautiful, intriguing, simple and uncomplicated. We don't want it overly busy, technical, or complex.
Nice to have
• MAYBE?? a broken heart being put back together.
Should not have
• No photo, no cartoon, no flowers, no couple (unless obscure and not gender specific).

```html
<!DOCTYPE html>
<html lang="en">
<head>
<meta charset="UTF-8">
<title>Mend the Quiet Hours — Book Cover</title>
<link rel="stylesheet" href="https://fonts.googleapis.com/css2?family=Barlow+Condensed:wght@300;700&family=Barlow+Semi+Condensed:wght@600&family=Permanent+Marker&display=swap">
<style>
  :root {
    --paper: #f3f2f0;
    --ink: #111111;
    --heart-red: #ff0a52;
    --scribble-grey: #4a4a4a;
    --title-white: #f2efeb;
  }
  * { margin: 0; padding: 0; box-sizing: border-box; }
  html, body {
    width: 750px;
    height: 1200px;
    overflow: hidden;
    background: var(--paper);
  }
  .cover {
    position: relative;
    width: 750px;
    height: 1200px;
    background:
      radial-gradient(ellipse at 30% 20%, rgba(255,255,255,0.7), transparent 60%),
      var(--paper);
    color: var(--ink);
    overflow: hidden;
  }
  .subtitle {
    position: absolute;
    top: 64px;
    left: 0;
    width: 100%;
    text-align: center;
    text-transform: uppercase;
  }
  .subtitle-light {
    display: block;
    font-family: "Barlow Condensed", sans-serif;
    font-weight: 300;
    font-size: 50px;
    line-height: 50px;
    letter-spacing: 1px;
  }
  .subtitle-bold {
    display: block;
    margin-top: 6px;
    font-family: "Barlow Condensed", sans-serif;
    font-weight: 700;
    font-size: 45px;
    line-height: 45px;
    letter-spacing: 1.5px;
  }
  .heart-artwork {
    position: absolute;
    left: 0;
    top: 184px;
    width: 750px;
    height: 800px;
    background: radial-gradient(ellipse 48% 46% at 50% 52%,
      var(--heart-red) 0%, var(--heart-red) 52%,
      rgba(74,74,74,0.55) 66%, rgba(74,74,74,0.18) 84%, transparent 100%);
  }
  .title {
    position: absolute;
    left: 0;
    top: 400px;
    width: 100%;
    text-align: center;
    font-family: "Permanent Marker", cursive;
    color: var(--title-white);
    text-transform: uppercase;
    transform: rotate(-10deg);
  }
  .title-line {
    display: block;
    line-height: 0.95;
  }
  .title-line.big { font-size: 104px; }
  .title-line.mid { font-size: 70px; }
  .author {
    position: absolute;
    top: 1100px;
    left: 0;
    width: 100%;
    text-align: center;
    font-family: "Barlow Semi Condensed", sans-serif;
    font-weight: 600;
    font-size: 40px;
    line-height: 44px;
    letter-spacing: 9px;
    text-transform: uppercase;
  }
</style>
</head>
<body>
  <main class="cover">
    <p class="subtitle">
      <span class="subtitle-light">For couples who</span>
      <span class="subtitle-bold">Don’t want to break up</span>
    </p>

    <div class="heart-artwork" role="img" aria-label="Illustration: a torn red paper heart mended with strips of tape, set over a tangle of dark scribbled lines"></div>

    <h1 class="title">
      <span class="title-line big">Mend the</span>
      <span class="title-line mid">Quiet</span>
      <span class="title-line big">Hours</span>
    </h1>

    <p class="author">Marla and Walter Dunmore, PhD</p>
  </main>
</body>
</html>
```